We need a wesbite for a new company based in London called: 'Belgrove Maids'. We supply the following services in private household: nanny, housekeeper, maternity nurse, driver, carer, companion and cleaner.
We would like to see designs that should communicate good ethics and high standard, quality services and professionalism.

I want a website something like: www.brightnestnursery.co.uk and http://www.tidyhearthstaff.co.uk/ I want the landing page should have at least 3 seconds intervals of changing photos of Asian (only) particularly Filipino (from the Philippines) Nanny with Children, Asian Housekeeper with apron cleaning, a photo of elderly in a wheelchair with the carer and a picture of a happy family with asian nanny in the background cleaning.

```html
<!DOCTYPE html>
<html lang="en">
<head>
<meta charset="utf-8">
<title>Belgrove Maids</title>
<link rel="stylesheet" href="https://fonts.googleapis.com/css2?family=Josefin+Sans:wght@300;400;600&family=Didact+Gothic&family=Marcellus+SC&display=swap">
<style>
:root{
  --blue:#1a8ad4;
  --blue-dark:#0f74b8;
  --yellow:#f5b301;
  --ink:#1d1d1d;
  --muted:#555;
  --grey-bg:#ececec;
  --footer:#222222;
  --footer-deep:#161616;
  --white:#ffffff;
}
*{margin:0;padding:0;box-sizing:border-box}
html,body{width:1200px;height:2736px;overflow:hidden;background:var(--white)}
body{position:relative;font-family:"Didact Gothic",sans-serif;color:var(--ink)}
.abs{position:absolute}
section,header,footer,.band{position:absolute;left:0;width:1200px}
h1,h2,h3,h4{font-weight:400;font-family:"Josefin Sans",sans-serif}

/* top bar */
.topbar{top:0;height:46px;border-top:3px solid var(--blue);font-size:14px;border-bottom:1px solid #e6e6e6}
.topbar .tag{left:82px;top:13px}
.topbar .contact{top:13px;display:flex;align-items:center;gap:8px;font-size:16px;white-space:nowrap}

/* header */
.site-header{top:46px;height:91px;background:var(--white)}
.brand{left:82px;top:14px;display:flex;align-items:center;gap:14px}
.brand-mark{width:56px;height:56px;border-radius:50%;background:var(--yellow)}
.brand-name{font-family:"Josefin Sans",sans-serif;font-size:30px;line-height:32px;color:var(--blue);letter-spacing:1px;text-transform:uppercase}
.nav{top:34px;font-size:15px;white-space:nowrap}

/* hero */
.hero{top:137px;height:498px;background:linear-gradient(100deg,#e9eef2 0%,#f4e6d3 35%,#d9c0a8 55%,#3f7fc4 75%,#8cc98f 100%)}
.hero-arrow{top:230px;width:38px;height:38px;background:#3a3a3a;opacity:.85;display:flex;align-items:center;justify-content:center}
.hero-caption{left:261px;top:381px;width:680px;height:75px;background:var(--blue);border-right:6px solid var(--yellow);color:var(--white);font-family:"Josefin Sans",sans-serif;font-size:34px;display:flex;align-items:center;justify-content:center;letter-spacing:.5px;white-space:nowrap}

/* services */
.services{top:635px;height:450px}
.services-band{top:0;left:0;width:1200px;height:250px;background:var(--yellow)}
.section-title{width:1200px;left:0;text-align:center;font-family:"Josefin Sans",sans-serif;font-size:37px;text-transform:uppercase}
.services .section-title{top:37px}
.services .section-title .lead{color:var(--white)}
.title-rule{height:2px}
.services-sub{top:122px;width:1200px;text-align:center;font-size:23px;font-family:"Josefin Sans",sans-serif}
.service{width:200px;margin-left:-100px;text-align:center;top:170px}
.service-ring{width:136px;height:136px;margin:0 auto;border-radius:50%;background:var(--white);border:5px solid var(--yellow);display:flex;align-items:center;justify-content:center}
.service-ring .icon-area{width:70px;height:70px;border-radius:50%;background:linear-gradient(#d8ecfa,#b6d9f3)}
.service h3{font-size:18px;margin-top:18px;color:var(--ink);white-space:nowrap}
.service p{font-size:13px;line-height:18px;color:var(--muted);margin-top:12px}

/* welcome */
.welcome{top:1085px;height:334px;background:var(--grey-bg)}
.welcome-photo{left:0;top:0;width:430px;height:334px;background:linear-gradient(90deg,#f1ede8 0%,#e6d7c9 45%,#ececec 100%)}
.welcome h2{left:430px;top:30px;font-size:37px;color:var(--ink)}
.welcome h2 span{color:var(--blue)}
.welcome .intro{left:430px;top:105px;width:690px;font-size:14px;line-height:19px;color:#333}
.feature{top:192px;width:200px}
.feature h4{font-size:20px;font-weight:600;display:flex;align-items:center;gap:10px}
.feature p{font-size:13px;line-height:18px;color:var(--muted);margin:4px 0 0 30px;width:140px}

/* cta */
.cta{top:1419px;height:117px;background:var(--blue)}
.cta p{left:82px;top:36px;font-family:"Josefin Sans",sans-serif;font-size:41px;color:var(--white);white-space:nowrap}
.cta-button{left:768px;top:22px;width:350px;height:72px;border-radius:36px;background:var(--yellow);border:3px solid var(--blue-dark);font-family:"Marcellus SC",serif;font-size:27px;color:var(--ink);display:flex;align-items:center;justify-content:center;letter-spacing:1px;white-space:nowrap}

/* why */
.why{top:1536px;height:438px;background:var(--white)}
.why .section-title{top:38px;color:var(--blue)}
.why .section-title .accent{color:var(--yellow)}
.hub{left:489px;top:149px;width:230px;height:230px;border-radius:50%;background:radial-gradient(circle at 50% 40%,#ffffff 0%,#f1f1f1 60%,#dcdcdc 100%);box-shadow:0 4px 10px rgba(0,0,0,.12);text-align:center}
.hub-mark{width:64px;height:64px;border-radius:50%;background:var(--yellow);margin:34px auto 0}
.hub-name{font-family:"Josefin Sans",sans-serif;font-size:21px;line-height:26px;letter-spacing:2px;color:#555;margin-top:18px;text-transform:uppercase}
.why-icon{width:56px;height:56px;margin:-28px 0 0 -28px;border-radius:50%;background:var(--blue);display:flex;align-items:center;justify-content:center;box-shadow:0 0 0 4px #e5f1fa}
.why-label{font-family:"Josefin Sans",sans-serif;font-size:20px;line-height:25px;color:var(--ink)}

/* testimonials */
.testimonials{top:1974px;height:383px;background:var(--grey-bg)}
.testimonial-photo{left:584px;top:0;width:616px;height:383px;background:linear-gradient(90deg,#ececec 0%,#e9ddd2 20%,#d8b99f 50%,#8fb574 80%,#a9c98b 100%)}
.testimonials h2{left:82px;top:80px;font-size:37px;color:var(--blue);text-transform:uppercase;white-space:nowrap}
.testimonials h2 span{color:var(--yellow)}
.quote{left:82px;top:136px;width:540px;font-size:13.5px;line-height:25.5px;color:#333;text-indent:38px}
.quote-mark{font-family:Georgia,serif;font-size:62px;color:#c9c9c9;line-height:1}
.quote-close{font-family:Georgia,serif;font-size:40px;color:#c9c9c9;line-height:0;vertical-align:-14px;margin-left:8px}

/* footer */
.site-footer{top:2357px;height:324px;background:var(--footer);color:#cfcfcf}
.footer-accent{left:0;top:0}
.site-footer h3{font-size:21px;color:#e6e6e6;font-family:"Josefin Sans",sans-serif}
.footer-col{top:50px}
.footer-col h3{padding-bottom:8px;border-bottom:1px solid #555;width:285px}
.quick-links{list-style:none;margin-top:14px;font-size:14px;line-height:28.5px}
.quick-links li::before{content:"›";color:var(--yellow);margin-right:8px}
.quick-links li.current{color:var(--yellow)}
.contact-list{list-style:none;margin-top:16px;font-size:15px}
.contact-list li{display:flex;gap:14px;margin-bottom:16px;line-height:18px;white-space:nowrap}
.contact-list strong{color:var(--white);font-weight:400}
.divider{left:285px;top:96px;width:1px;height:190px;background:#3a3a3a}
.hours{left:861px;top:40px;color:var(--ink)}
.hours-mark{width:100px;height:100px;border-radius:50%;background:#2a2a2a;margin-left:30px}
.site-footer .hours h3{color:var(--ink);font-size:22px;margin-top:14px}
.hours p{font-size:14px;line-height:19px;margin-top:8px}
.social{display:flex;gap:12px;margin-top:12px}
.social span{width:35px;height:35px;border-radius:50%;background:var(--blue);display:block}
.copyright{top:2681px;height:55px;background:var(--footer-deep);color:#d0d0d0;font-size:14px;text-align:center;line-height:55px}
</style>
</head>
<body>

<div class="band topbar">
  <span class="abs tag">Supplying Maid Services in Private Household</span>
  <span class="abs contact" style="left:736px">
    <svg width="18" height="18" viewBox="0 0 24 24"><circle cx="12" cy="12" r="10.5" fill="none" stroke="#1a8ad4" stroke-width="2"/><path d="M8.5 7.5l2 2-1 1.2c.7 1.5 1.8 2.6 3.3 3.3l1.2-1 2 2-1.2 1.3c-3.5-.4-6.9-3.8-7.3-7.3z" fill="#1a8ad4"/></svg>
    020-7946-0318
  </span>
  <span class="abs contact" style="left:903px">
    <svg width="18" height="14" viewBox="0 0 24 18"><rect x="1" y="1" width="22" height="16" fill="none" stroke="#1a8ad4" stroke-width="2"/><path d="M1 1l11 9 11-9" fill="none" stroke="#1a8ad4" stroke-width="2"/></svg>
    info@belgrovemaids.com
  </span>
</div>

<header class="site-header">
  <div class="abs brand">
    <span class="brand-mark"></span>
    <span class="brand-name">Belgrove<br>Maids</span>
  </div>
  <svg class="abs" style="left:614px;top:28px" width="26" height="24" viewBox="0 0 26 24"><path d="M13 2L1 13h4v10h6v-7h4v7h6V13h4z" fill="#1a8ad4"/></svg>
  <span class="abs nav" style="left:671px">About Us</span>
  <span class="abs nav" style="left:770px">Services</span>
  <span class="abs nav" style="left:863px">Training</span>
  <span class="abs nav" style="left:956px">Career</span>
  <span class="abs nav" style="left:1040px">Contact Us</span>
</header>

<section class="hero" role="img" aria-label="Photo of a smiling nanny playing finger puppets with a toddler at a colourful play table">
  <div class="abs hero-arrow" style="left:0"><svg width="14" height="14" viewBox="0 0 14 14"><path d="M10 1L3 7l7 6z" fill="#fff"/></svg></div>
  <div class="abs hero-arrow" style="left:1162px"><svg width="14" height="14" viewBox="0 0 14 14"><path d="M4 1l7 6-7 6z" fill="#fff"/></svg></div>
  <div class="abs hero-caption">TAKING CARE OF YOUR EVERY NEEDS</div>
</section>

<section class="services">
  <div class="abs services-band"></div>
  <h2 class="abs section-title"><span class="lead">Our</span> Services</h2>
  <div class="abs title-rule" style="left:469px;top:95px;width:290px;background:#fff"></div>
  <p class="abs services-sub">We Are Based In London, UK Supplying The Following Services In Private Households</p>

  <div class="abs service" style="left:148px"><div class="service-ring"><span class="icon-area" role="img" aria-label="Nanny icon"></span></div><h3>Nanny</h3><p>Lorem ipsum dolor sit<br>amet, consectetuer</p></div>
  <div class="abs service" style="left:328px"><div class="service-ring"><span class="icon-area" role="img" aria-label="Housekeeper icon"></span></div><h3>Housekeeper</h3><p>Lorem ipsum dolor sit<br>amet, consectetuer</p></div>
  <div class="abs service" style="left:509px"><div class="service-ring"><span class="icon-area" role="img" aria-label="Driver icon"></span></div><h3>Driver</h3><p>Lorem ipsum dolor sit<br>amet, consectetuer</p></div>
  <div class="abs service" style="left:689px"><div class="service-ring"><span class="icon-area" role="img" aria-label="Carer icon"></span></div><h3>Carer</h3><p>Lorem ipsum dolor sit<br>amet, consectetuer</p></div>
  <div class="abs service" style="left:872px"><div class="service-ring"><span class="icon-area" role="img" aria-label="Maternity nurse icon"></span></div><h3>Maternity Nurse</h3><p>Lorem ipsum dolor sit<br>amet, consectetuer</p></div>
  <div class="abs service" style="left:1054px"><div class="service-ring"><span class="icon-area" role="img" aria-label="Companion and cleaner icon"></span></div><h3>Companion &amp; Cleaner</h3><p>Lorem ipsum dolor sit<br>amet, consectetuer</p></div>
</section>

<section class="welcome">
  <div class="abs welcome-photo" role="img" aria-label="Photo of a mother lying on a bed with two young children and a teddy bear"></div>
  <h2 class="abs">Welcome To <span>Belgrove Maids</span></h2>
  <p class="abs intro">Lorem ipsum dolor sit amet, consectetuer adipiscing elit, sed diam nonummy nibh euismod tincidunt ut laoreet dolore magna aliquam erat volutpat. Ut wisi enim ad minim veniam, quis nostrud exerci tation ullamcorper suscipit lobortis nisl ut aliquip ex ea commodo consequat.</p>
  <div class="abs feature" style="left:430px"><h4><svg width="20" height="20" viewBox="0 0 20 20"><circle cx="10" cy="10" r="9" fill="#f5b301"/><path d="M5.5 10.5l3 3 6-6" fill="none" stroke="#fff" stroke-width="2.2"/></svg>We Check</h4><p>Lorem ipsum dolor sit amet, consectetuer adipiscing elit.</p></div>
  <div class="abs feature" style="left:644px"><h4><svg width="20" height="20" viewBox="0 0 20 20"><circle cx="10" cy="10" r="9" fill="#f5b301"/><path d="M5.5 10.5l3 3 6-6" fill="none" stroke="#fff" stroke-width="2.2"/></svg>We Listen</h4><p>Lorem ipsum dolor sit amet, consectetuer adipiscing elit.</p></div>
  <div class="abs feature" style="left:857px"><h4><svg width="20" height="20" viewBox="0 0 20 20"><circle cx="10" cy="10" r="9" fill="#f5b301"/><path d="M5.5 10.5l3 3 6-6" fill="none" stroke="#fff" stroke-width="2.2"/></svg>We Care</h4><p>Lorem ipsum dolor sit amet, consectetuer adipiscing elit.</p></div>
</section>

<section class="cta">
  <p class="abs">Need A Carer for your loved one?</p>
  <div class="abs cta-button">Get In Touch Today</div>
</section>

<section class="why">
  <h2 class="abs section-title">Why <span class="accent">Choose Us</span></h2>
  <div class="abs" style="left:357px;top:97px;width:518px;height:1px;background:#d6d6d6"></div>
  <div class="abs" style="left:452px;top:96px;width:325px;height:3px;background:var(--blue)"></div>

  <svg class="abs" style="left:0;top:0" width="1200" height="438" viewBox="0 0 1200 438">
    <g fill="none" stroke="#d5d5d5" stroke-width="1.5">
      <path d="M420 184H470L505 214"/>
      <path d="M420 335H470L505 305"/>
      <path d="M782 184H732L697 214"/>
      <path d="M782 335H732L697 305"/>
    </g>
  </svg>

  <div class="hub abs"><div class="hub-mark"></div><div class="hub-name">Belgrove<br>Maids</div></div>

  <div class="abs why-icon" style="left:392px;top:184px"><svg width="26" height="26" viewBox="0 0 26 26"><path d="M5 13l5 5 11-11" fill="none" stroke="#fff" stroke-width="3"/></svg></div>
  <div class="abs why-icon" style="left:392px;top:335px"><svg width="26" height="26" viewBox="0 0 26 26"><circle cx="13" cy="13" r="10" fill="none" stroke="#fff" stroke-width="2.5"/><path d="M13 7v6l4 3" fill="none" stroke="#fff" stroke-width="2.5"/></svg></div>
  <div class="abs why-icon" style="left:810px;top:184px"><svg width="26" height="26" viewBox="0 0 26 26"><path d="M13 2l3.3 7 7.7.8-5.8 5.2 1.7 7.6L13 18.7 6.1 22.6l1.7-7.6L2 9.8 9.7 9z" fill="#fff"/></svg></div>
  <div class="abs why-icon" style="left:810px;top:335px"><svg width="26" height="26" viewBox="0 0 26 26"><path d="M13 22S3 15.5 3 9.5A5 5 0 0 1 13 7a5 5 0 0 1 10 2.5C23 15.5 13 22 13 22z" fill="#fff"/></svg></div>

  <div class="abs why-label" style="left:180px;top:166px;width:152px;text-align:right">We Have<br>Trained Staff</div>
  <div class="abs why-label" style="left:180px;top:317px;width:152px;text-align:right">Fast Work<br>And Help</div>
  <div class="abs why-label" style="left:866px;top:166px">Year of<br>Experience</div>
  <div class="abs why-label" style="left:866px;top:317px">Satisfied<br>Clients</div>
</section>

<section class="testimonials">
  <div class="abs testimonial-photo" role="img" aria-label="Photo of a happy family with parents carrying two children piggyback outdoors"></div>
  <h2 class="abs">What Our <span>Customers Say</span></h2>
  <span class="abs quote-mark" style="left:78px;top:128px">&ldquo;</span>
  <p class="abs quote">Lorem ipsum dolor sit amet, consectetuer adipiscing elit, sed diam nonummy nibh euismod tincidunt ut laoreet dolore magna aliquam erat volutpat. Ut wisi enim ad minim veniam, quis nostrud exerci tationmo ullamcorper suscipit lobortis nisl ut aliquip commodo consequat. Duis autem vel eum iriure dolor in hendni vulputate velit esse molestie consequat.Lorem ipsum dolor sit amet, consectetuer adipiscing elit, sed diam nonummy nibh euismod tincduntk ut laoreet dolore magna aliquam erat volutpat. Ut wisi enim ad minim veniam.<span class="quote-close">&rdquo;</span></p>
</section>

<footer class="site-footer">
  <svg class="abs footer-accent" width="1200" height="324" viewBox="0 0 1200 324"><path d="M775 0H1200V324H698z" fill="#f5b301"/></svg>

  <div class="abs footer-col" style="left:80px">
    <h3 style="width:200px">Quick Links</h3>
    <ul class="quick-links">
      <li class="current">Home</li>
      <li>About Us</li>
      <li>Services</li>
      <li>Training</li>
      <li>Careers</li>
      <li>Contact Us</li>
    </ul>
  </div>
  <div class="abs divider"></div>

  <div class="abs footer-col" style="left:376px">
    <h3>Contact Detail</h3>
    <ul class="contact-list">
      <li><svg width="14" height="18" viewBox="0 0 14 18"><path d="M7 1a6 6 0 0 1 6 6c0 4.5-6 10-6 10S1 11.5 1 7a6 6 0 0 1 6-6z" fill="#f5b301"/><circle cx="7" cy="7" r="2.2" fill="#222"/></svg><span style="font-size:14px"><strong>Belgrove Maids</strong><br>Larchmere Row 18<br>SW3 4QT London</span></li>
      <li><svg width="16" height="16" viewBox="0 0 24 24"><path d="M5 2l4 4-2 2.5c1.3 3 3.5 5.2 6.5 6.5L16 13l4 4-2.5 3C10 19.5 4.5 14 4 6.5z" fill="#f5b301"/></svg>(020) 7946 0318</li>
      <li><svg width="16" height="16" viewBox="0 0 24 24"><rect x="6" y="2" width="12" height="6" fill="#f5b301"/><rect x="2" y="9" width="20" height="9" rx="1" fill="#f5b301"/><rect x="6" y="15" width="12" height="7" fill="#f5b301" stroke="#222" stroke-width="1.5"/></svg>(020) 7946 0319</li>
      <li><svg width="16" height="13" viewBox="0 0 24 18"><rect x="1" y="1" width="22" height="16" fill="#f5b301"/><path d="M1 1l11 9 11-9" fill="none" stroke="#222" stroke-width="2"/></svg>hello@belgrovemaids.com</li>
    </ul>
  </div>

  <div class="abs hours">
    <div class="hours-mark"></div>
    <h3>Working Hours</h3>
    <p>Monday - Saturday: 09: 00 am<br>to 7:00 am</p>
    <p style="margin-top:6px">Sunday : Closed</p>
    <div class="social"><span></span><span></span><span></span></div>
  </div>
</footer>

<div class="band copyright">Copyright © 2016 Belgrove Maids . All Rights Reserved.</div>

</body>
</html>
```